Mrs Tidwell

I would like an A5 size two sided flyer designed. This flyer is for handing out and pinningon notice boards. The brochure is prodominately for a male audience and I would prefer that it is not too 'busy'.

My business is complete housekeeping business targeted at fly in fly out miners in WA Australia. The business designs customised packages for the individual or household and completing all work while the person is at work. It is about making life simple for them so when they come home on their break all of the chores are completed and they don't have to do anything. Payments are made by Direct debit on a weekly or fortninghtly basis.

I am looking for bookings to start early 2013 for all areas of Perth.

10% discount on servcies if they included in a package with a regular house clean.

I would not like to see my exact wording from here just put into a design I would like the designer to add some thought to the design..

Please see below a list of my services.

House Cleaning
Regular clean
Spring clean
End of lease or moving clean

Inside
Linen washed
Clothes washed
Clothes ironed
Breakfast basket (Continental)
Breakfast basket (Deluxe)
Dishwashing/drying
Wheelie bins put out and in
Wheelie bins cleaned
Mail collected
Drinks stacked in fridge
Garage cleaned
Windows cleaned
Fridge Cleaned
Oven cleaned
Cupboards cleaned and organised
Carpets steam cleaned
Plants watered

Outside
Lawns mowed
Edges trimmed
Extra garden services
Windows washed
Cobwebs removed
Gutters cleaned
Reticulation maintenance/repairs
Patio area cleaned
Lawn and garden fertilising
Rubbish removal

Other
Alcohol delivery
Meet tradesperson/suppliers
Grocery shopping+
Run errands+
Bills paid+
Send or collect parcels+
Dry cleaning dropped off+
Clothing repairs alterations
Present shopping wrapping, card selection+

Your car
Car washed and vacuumed
Car detailed
Car drop off and collected for service and/or repairs+

Prodominately males and Miners

Shopping

```html
<!DOCTYPE html>
<html lang="en">
<head>
<meta charset="utf-8">
<title>Mrs Tidwell – A5 Flyer</title>
<link rel="stylesheet" href="https://fonts.googleapis.com/css2?family=Ubuntu:ital,wght@0,400;0,500;0,700;1,400&family=Delius&display=swap">
<style>
  :root {
    --red: #c4161c;
    --red-dark: #8e0f13;
    --ink: #1f1f1f;
    --charcoal: #2b2b2b;
    --paper: #f1f1f1;
    --white: #ffffff;
    --stage: #e9e9e9;
  }
  * { box-sizing: border-box; margin: 0; padding: 0; }
  html, body { width: 1200px; height: 717px; overflow: hidden; }
  body {
    background: var(--stage);
    font-family: "Ubuntu", sans-serif;
    color: var(--ink);
    position: relative;
  }
  .flyer {
    position: absolute;
    top: 47px;
    width: 440px;
    height: 622px;
    overflow: hidden;
    box-shadow: 0 10px 30px rgba(0,0,0,.25);
  }
  .flyer--front { left: 130px; background: linear-gradient(180deg, #fbfbfb, #e8e8e8); }
  .flyer--back { left: 630px; background: var(--charcoal); }

  /* ---------- FRONT ---------- */
  .front-title { position: absolute; left: 24px; top: 20px; width: 280px; }
  .front-title .brand {
    font-size: 34px; font-weight: 700; color: var(--ink); line-height: 1.1;
  }
  .front-title .tagline { font-size: 16px; font-weight: 400; margin-top: 8px; }

  .intro {
    position: absolute; left: 24px; top: 118px; width: 205px;
    font-size: 15px; font-weight: 700; line-height: 1.35;
  }
  .intro .brand-word { color: var(--red); }

  .hero-figure {
    position: absolute; left: 240px; top: 96px; width: 176px; height: 220px;
    border-radius: 12px;
    background: linear-gradient(180deg, #e6e6e6, #d2d2d2);
  }

  .front-shapes { position: absolute; inset: 0; }

  .offer {
    position: absolute; left: 20px; top: 334px; width: 208px; height: 104px;
    background: var(--charcoal); border: 3px solid var(--red); border-radius: 10px;
    color: var(--white); text-align: center; padding: 12px 10px;
    box-shadow: 0 3px 8px rgba(0,0,0,.4);
  }
  .offer .headline { font-size: 26px; font-weight: 700; line-height: 1.1; }
  .offer .detail { font-size: 14px; line-height: 1.25; margin-top: 4px; }

  .specialities { position: absolute; left: 248px; top: 352px; width: 175px; color: var(--white); }
  .specialities h3 { font-size: 14px; font-weight: 700; text-decoration: underline; margin-bottom: 6px; }

  .ticks { list-style: none; }
  .ticks li { position: relative; padding-left: 17px; }
  .ticks li::before {
    content: ""; position: absolute; left: 0; top: 2px; width: 11px; height: 11px; border-radius: 50%;
    background: var(--red);
  }
  .ticks li::after {
    content: ""; position: absolute; left: 3.5px; top: 4px; width: 3px; height: 5px;
    border: solid var(--white); border-width: 0 1.5px 1.5px 0; transform: rotate(45deg);
  }
  .ticks--light li::before { background: var(--white); }
  .ticks--light li::after { border-color: var(--red); }
  .specialities .ticks li { font-size: 11px; line-height: 1.6; }

  .promise {
    position: absolute; left: 36px; top: 452px; width: 210px; text-align: center;
    color: var(--white); font-weight: 700; line-height: 1.05;
  }
  .promise .big { font-size: 38px; letter-spacing: 1px; }
  .promise .small { font-size: 24px; }

  .front-footer {
    position: absolute; left: 0; bottom: 0; width: 100%; height: 70px;
    background: var(--charcoal); color: var(--white); text-align: center; padding-top: 12px;
  }
  .front-footer .call { font-size: 17px; font-weight: 700; }
  .front-footer .area { font-size: 11px; margin-top: 8px; color: #ddd; }

  /* ---------- BACK ---------- */
  .back-heading {
    color: var(--white); font-family: "Delius", cursive; font-size: 19px; font-weight: 400;
    text-align: center; padding-top: 12px;
  }
  .back-panel {
    position: absolute; left: 12px; right: 12px; top: 44px; height: 488px;
    background: var(--paper); overflow: hidden;
  }
  .back-figure {
    position: absolute; left: 110px; top: 80px; width: 210px; height: 290px;
    background: radial-gradient(ellipse at 50% 45%, rgba(0,0,0,.07), transparent 70%);
  }
  .back-panel .ticks li { font-family: "Delius", cursive; font-size: 11px; line-height: 1.45; }
  .cleans { display: grid; grid-template-columns: 1fr 1fr; padding: 8px 14px 4px; position: relative; }
  .back-panel .cleans li { font-size: 14px; }
  .section-bar {
    position: relative; background: var(--red); color: var(--white); font-weight: 500; font-size: 14px;
    padding: 3px 0 3px 26px; margin: 4px 0 5px; box-shadow: 0 2px 3px rgba(0,0,0,.35);
  }
  .section-bar::before {
    content: ""; position: absolute; left: 8px; top: 6px; width: 11px; height: 11px; border-radius: 50%;
    background: var(--white);
  }
  .section-bar::after {
    content: ""; position: absolute; left: 12px; top: 8px; width: 3px; height: 5px;
    border: solid var(--red); border-width: 0 1.5px 1.5px 0; transform: rotate(45deg);
  }
  .two-col { display: grid; grid-template-columns: 1fr 1fr; column-gap: 10px; padding: 0 14px; position: relative; }
  .bottom-row { display: grid; grid-template-columns: 1fr 1fr; column-gap: 8px; position: relative; }
  .other-list { display: grid; grid-template-columns: 1fr 1fr; column-gap: 4px; padding: 0 10px; }
  .back-panel .other-list li { font-size: 9.5px; line-height: 1.7; }
  .car-list { padding: 0 10px; }

  .discount-strip {
    position: absolute; left: 0; right: 0; top: 540px; background: var(--red); color: var(--white);
    font-size: 11px; text-align: center; padding: 5px 0;
  }
  .back-footer {
    position: absolute; left: 0; right: 0; bottom: 0; height: 56px; color: #ddd; font-size: 11px;
    display: flex; justify-content: space-between; align-items: center; padding: 0 16px;
  }
  .back-footer .web { text-align: right; }
</style>
</head>
<body>

<section class="flyer flyer--front" aria-label="Flyer front">
  <svg class="front-shapes" width="440" height="622" viewBox="0 0 440 622" aria-hidden="true">
    <path d="M0 372 C 140 350, 300 330, 440 290 L 440 622 L 0 622 Z" fill="#8e0f13"/>
    <path d="M0 382 C 140 360, 300 340, 440 302 L 440 622 L 0 622 Z" fill="#c4161c"/>
  </svg>

  <header class="front-title">
    <h1 class="brand">Mrs Tidwell</h1>
    <p class="tagline">Who's doin your home?</p>
  </header>

  <p class="intro">Don't do chores during your time off, customise a package to suit your exact needs and let <span class="brand-word">Mrs Tidwell</span> do it for you.</p>

  <div class="hero-figure" role="img" aria-label="Illustration of a housekeeper silhouette dusting"></div>

  <div class="offer">
    <div class="headline">Get 10% off</div>
    <div class="detail">Include in a package with a regular house clean.</div>
  </div>

  <div class="specialities">
    <h3>Specialising in:</h3>
    <ul class="ticks ticks--light">
      <li>ALL housekeeping services</li>
      <li>Inside and out</li>
      <li>Customised packages</li>
      <li>Share houses</li>
      <li>Keeping life simple</li>
    </ul>
  </div>

  <div class="promise">
    <div class="big">SO YOU</div>
    <div class="small">Don't Have To<br>Do A Thing</div>
  </div>

  <footer class="front-footer">
    <div class="call">Call: 08-6100-2745 or 0412 000 318</div>
    <div class="area">Servicing all areas of Perth. &nbsp;|&nbsp; Taking bookings now for early 2013.</div>
  </footer>
</section>

<section class="flyer flyer--back" aria-label="Flyer back">
  <h2 class="back-heading">Ways we help make your life easy:</h2>

  <div class="back-panel">
    <div class="back-figure" role="img" aria-label="Faint housekeeper silhouette decoration"></div>

    <ul class="ticks cleans">
      <li>Moving Clean</li>
      <li>End of lease cleaning</li>
      <li>Regular Clean</li>
      <li>Spring clean</li>
    </ul>

    <div class="section-bar">Inside</div>
    <div class="two-col">
      <ul class="ticks">
        <li>Linen washed</li>
        <li>Clothes washed</li>
        <li>Clothes ironed</li>
        <li>Breakfast basket (Continental)</li>
        <li>Breakfast basket (Deluxe)</li>
        <li>Dishwashing/drying</li>
        <li>Wheelie bins put out and in</li>
        <li>Wheelie bins cleaned</li>
        <li>Mail collected</li>
      </ul>
      <ul class="ticks">
        <li>Drinks stacked in fridge</li>
        <li>Garage cleaned</li>
        <li>Windows cleaned</li>
        <li>Fridge Cleaned</li>
        <li>Oven cleaned</li>
        <li>Cupboards cleaned and organised</li>
        <li>Carpets steam cleaned</li>
        <li>Plants watered</li>
      </ul>
    </div>

    <div class="section-bar">Outside</div>
    <div class="two-col">
      <ul class="ticks">
        <li>Lawns mowed</li>
        <li>Edges trimmed</li>
        <li>Extra garden services</li>
        <li>Windows washed</li>
        <li>Reticulation maintenance/ repairs</li>
      </ul>
      <ul class="ticks">
        <li>Cobwebs removed</li>
        <li>Gutters cleaned</li>
        <li>Patio area cleaned</li>
        <li>Rubbish removal</li>
        <li>Lawn and garden fertilising</li>
      </ul>
    </div>

    <div class="bottom-row">
      <div>
        <div class="section-bar">Other</div>
        <ul class="ticks other-list">
          <li>Bills paid</li>
          <li>Run errands</li>
          <li>Meet trades</li>
          <li>Grocery shopping</li>
          <li>Clothing repairs</li>
          <li>Parcels sent</li>
          <li>Dry cleaning</li>
          <li>Alcohol delivery</li>
        </ul>
      </div>
      <div>
        <div class="section-bar">Your car</div>
        <ul class="ticks car-list">
          <li>Car detailed</li>
          <li>Car washed and vacuumed</li>
          <li>Car drop off and collected for service and/or repairs</li>
        </ul>
      </div>
    </div>
  </div>

  <div class="discount-strip">A 10% discount for services provided with regular house cleaning.</div>

  <footer class="back-footer">
    <div>Other services may be<br>accommodated on request.</div>
    <div class="web">See website for full details<br>www.mrstidwell.com.au</div>
  </footer>
</section>

</body>
</html>
```